Banner Designs for Drone Defense Ad Campaign

Corvane is a security consulting and services company that offers a service called SkyMindful. SkyMindful helps our customers identify security risks from drones and develops comprehensive protection programs. We are looking for a designer to create a banner ad in three sizes for our campaign.
Target Market(s)
Our campaign is geared to the sports and entertainment industry, specifically large event venues and their security operation.
Industry/Entity Type
Security
Font styles to use
Other font styles liked:
- Raleway
Requirements
Must have
- Banner Objective
The visual and textual content of the banner should prompt the viewer to quickly identify the service offered and the information that is available to download.
Banner Design
Logo: SkyMindful logo
Call to Action Button in Red: Get It Here (On Right or or Upper Right)
Title in Larger Font: Guide to UAS Risk Mitigation
Subtitle in smaller Font: 5 Steps to Develop Your Comprehensive UAS Defense Program
Background: Stadium with a drone flying in foreground
Font: Raleway
Banner Sizes
1 - 1200x670 pixels
2 - 1510x196 pixels
3 - 1200x628 pixels

```html
<!DOCTYPE html>
<html lang="en">
<head>
<meta charset="utf-8">
<title>SkyMindful Banner Set – Guide to UAS Risk Mitigation</title>
<link href="https://fonts.googleapis.com/css2?family=Raleway:wght@400;500;600;800&display=swap" rel="stylesheet">
<style>
  :root {
    --stage-blue: #3478bb;
    --stage-grey: #a1a1a1;
    --brand-blue: #2f7bc4;
    --white: #ffffff;
    --cta-red: #e10a0a;
    --photo-top: #0a0c12;
    --photo-mid: #101b30;
    --photo-bottom: #1d2f55;
    --stadium-glow: #3a2f7a;
  }
  * { margin: 0; padding: 0; box-sizing: border-box; }
  html, body { width: 1099px; height: 1200px; overflow: hidden; background: var(--stage-grey); }
  .stage {
    position: relative;
    width: 1692px; height: 1848px;
    transform: scale(0.6495); transform-origin: 0 0;
    font-family: 'Raleway', sans-serif;
  }
  .stage-backdrop { position: absolute; inset: 0; }
  .banner {
    position: absolute; overflow: hidden;
    box-shadow: 0 10px 30px rgba(0,0,0,.45);
  }
  .banner-photo {
    position: absolute; inset: 0;
    background:
      radial-gradient(ellipse 45% 35% at 58% 78%, var(--stadium-glow) 0%, transparent 70%),
      linear-gradient(180deg, var(--photo-top) 0%, var(--photo-mid) 40%, var(--photo-bottom) 100%);
  }
  .banner--large-a { left: 91px; top: 150px; width: 1200px; height: 670px; }
  .banner--leaderboard { left: 91px; top: 846px; width: 1510px; height: 196px; }
  .banner--large-b { left: 91px; top: 1070px; width: 1200px; height: 628px; }

  .brand { position: absolute; left: 70px; color: var(--white); }
  .brand-name { display: block; font-weight: 500; font-size: 46px; line-height: 1; color: var(--brand-blue); }
  .brand-byline { display: block; text-align: right; font-weight: 400; font-size: 24px; margin-top: 8px; color: var(--white); }

  .headline { position: absolute; left: 30px; font-weight: 800; line-height: 1; letter-spacing: -1px; }
  .headline .accent { display: block; color: var(--brand-blue); font-size: 76px; }
  .headline .strong { display: block; color: var(--white); font-size: 76px; margin-top: 10px; }
  .subhead { position: absolute; left: 30px; color: var(--white); font-weight: 500; font-size: 43px; line-height: 54px; }

  .cta {
    position: absolute; left: 31px;
    display: flex; align-items: center; justify-content: center; gap: 8px;
    width: 221px; height: 63px; border-radius: 32px;
    background: var(--cta-red); color: var(--white);
    font-weight: 800; font-size: 18px; letter-spacing: -.3px;
  }
  .cta svg { width: 17px; height: 17px; }

  .leaderboard-brand { position: absolute; left: 70px; top: 50px; }
  .leaderboard-brand .brand-name { font-size: 44px; }
  .leaderboard-brand .brand-byline { font-size: 23px; margin-top: 6px; }
  .leaderboard-copy { position: absolute; left: 408px; top: 22px; width: 700px; text-align: center; }
  .leaderboard-title { font-weight: 800; font-size: 46px; line-height: 1; letter-spacing: -.5px; color: var(--white); }
  .leaderboard-title .accent { color: var(--brand-blue); }
  .leaderboard-sub { margin-top: 14px; font-weight: 500; font-size: 22px; color: var(--white); }
  .leaderboard-cta {
    position: absolute; left: 675px; top: 131px; width: 161px; height: 45px; border-radius: 23px;
    display: flex; align-items: center; justify-content: center; gap: 6px;
    background: var(--cta-red); color: var(--white); font-weight: 800; font-size: 12px;
  }
  .leaderboard-cta svg { width: 12px; height: 12px; }
</style>
</head>
<body>
<div class="stage">
  <svg class="stage-backdrop" viewBox="0 0 1692 1848" width="1692" height="1848" aria-hidden="true">
    <rect width="1692" height="1848" fill="var(--stage-grey)"/>
    <ellipse cx="760" cy="260" rx="1360" ry="1330" fill="var(--stage-blue)"/>
  </svg>

  <section class="banner banner--large-a">
    <div class="banner-photo" role="img" aria-label="Night aerial photo of an illuminated stadium with a quadcopter drone flying in the foreground"></div>
    <div class="brand" style="top:92px"><span class="brand-name">SkyMindful</span><span class="brand-byline">By Corvane</span></div>
    <h1 class="headline" style="top:225px"><span class="accent">GUIDE TO UAS</span><span class="strong">RISK MITIGATION</span></h1>
    <p class="subhead" style="top:412px">5 Steps to Develop Your Comprehensive<br>UAS Defense Program</p>
    <a class="cta" style="top:556px">GET IT HERE
      <svg viewBox="0 0 16 16"><circle cx="8" cy="8" r="8" fill="#fff"/><path d="M6.5 4.5 10 8l-3.5 3.5" stroke="var(--cta-red)" stroke-width="2.2" fill="none"/></svg>
    </a>
  </section>

  <section class="banner banner--leaderboard">
    <div class="banner-photo" role="img" aria-label="Night aerial photo of an illuminated stadium with a quadcopter drone flying at the right"></div>
    <div class="brand leaderboard-brand"><span class="brand-name">SkyMindful</span><span class="brand-byline">By Corvane</span></div>
    <div class="leaderboard-copy">
      <h2 class="leaderboard-title"><span class="accent">GUIDE TO UAS</span> RISK MITIGATION</h2>
      <p class="leaderboard-sub">5 Steps to Develop Your Comprehensive UAS Defense Program</p>
    </div>
    <a class="leaderboard-cta">GET IT HERE
      <svg viewBox="0 0 16 16"><circle cx="8" cy="8" r="8" fill="#fff"/><path d="M6.5 4.5 10 8l-3.5 3.5" stroke="var(--cta-red)" stroke-width="2.2" fill="none"/></svg>
    </a>
  </section>

  <section class="banner banner--large-b">
    <div class="banner-photo" role="img" aria-label="Night aerial photo of an illuminated stadium with a quadcopter drone flying in the foreground"></div>
    <div class="brand" style="top:72px"><span class="brand-name">SkyMindful</span><span class="brand-byline">By Corvane</span></div>
    <h2 class="headline" style="top:205px"><span class="accent">GUIDE TO UAS</span><span class="strong">RISK MITIGATION</span></h2>
    <p class="subhead" style="top:392px">5 Steps to Develop Your Comprehensive<br>UAS Defense Program</p>
    <a class="cta" style="top:535px">GET IT HERE
      <svg viewBox="0 0 16 16"><circle cx="8" cy="8" r="8" fill="#fff"/><path d="M6.5 4.5 10 8l-3.5 3.5" stroke="var(--cta-red)" stroke-width="2.2" fill="none"/></svg>
    </a>
  </section>
</div>
</body>
</html>
```